Webdesign für SEO-Agentur
Zielgruppe
Wir bieten kleinen und mittelständischen Unternehmen Suchmaschinenoptimierung zum fairen Preis mit Erfolgsgarantie an. Unsere Zielgruppe sind Unternehmer die bisher wenig oder gar keine Erfahrungen mit SEO hatten. Wir möchten Unternehmen dabei helfen ihren digitalen Auftritt sowie dessen Sichtbarkeit zu verbessern um neue Kunden zu finden.
Aufgabenstellung
- seriöses und modernes Design bei gleichzeitig ansprechender Gestaltung
- passend zum Namen möchten wir, dass die Website einen leichten wissenschaftlichen/chemischen Touch erhält. Beachten Sie daher unsere Skizze zur Schritt für Schritt Darstellung. Weitere kleine Hinweise in Richtung Chemie oder Wissenschaft können und sollen eingebaut werden.
- vorerst nur Landing-Page, daher keine Navigation nötig. Wir erwarten eine vollständige Desktop sowie Mobilversion in Ihrem Design.
- Einhaltung der vorgegebenen Inhalte
- keine langweiligen Standard-Designs, auch besondere Seiten können seriös sein
- Header ist für Portrait der Mitarbeiter reserviert und benötigt daher eine gewisse freie Fläche

```html
<!DOCTYPE html>
<html lang="de">
<head>
<meta charset="utf-8">
<title>ValenzWerk – SEO-Agentur</title>
<link href="https://fonts.googleapis.com/css2?family=Lato:wght@300;400;700&display=swap" rel="stylesheet">
<style>
  :root {
    --navy: #13396a;
    --red: #e8173f;
    --bg: #f7f7f8;
    --text: #6b6f78;
    --muted: #9a9ea6;
    --card: #ffffff;
  }
  * { margin: 0; padding: 0; box-sizing: border-box; }
  html, body { width: 1200px; height: 3288px; overflow: hidden; }
  body { font-family: 'Lato', sans-serif; background: var(--bg); color: var(--text); position: relative; }
  .abs { position: absolute; }
  .sidebar-line { left: 40px; top: 0; width: 1px; height: 3288px; background: #e6e7ea; }
  .dots { left: 15px; top: 225px; display: flex; flex-direction: column; gap: 15px; }
  .dots span { width: 9px; height: 9px; border-radius: 50%; border: 1px solid #c9ccd2; }
  .dots span.active { background: var(--red); border-color: var(--red); }
  .shape { position: absolute; left: 0; top: 0; }
  .logo { left: 137px; top: 56px; display: flex; align-items: center; gap: 8px; font-size: 30px; font-weight: 700; color: var(--navy); }
  .logo i { width: 8px; height: 8px; border-radius: 50%; background: var(--red); }
  .hero-title { left: 137px; top: 226px; font-size: 32px; font-weight: 700; color: var(--navy); line-height: 37px; }
  .hero-sub { left: 137px; top: 306px; font-size: 20px; font-weight: 300; color: var(--muted); line-height: 28px; }
  .lead-form { left: 137px; top: 398px; width: 450px; height: 44px; background: #fff; border-radius: 22px; box-shadow: 0 4px 14px rgba(0,0,0,.06); display: flex; justify-content: space-between; align-items: center; }
  .lead-form .field { padding-left: 17px; font-size: 12px; font-style: italic; color: #aaa; font-weight: 300; }
  .btn { background: var(--red); color: #fff; border-radius: 24px; font-size: 14px; font-weight: 400; display: flex; align-items: center; justify-content: center; }
  .lead-form .btn { width: 176px; height: 44px; font-size: 13px; }
  .center { left: 0; width: 1200px; text-align: center; }
  .section-title { font-size: 31px; font-weight: 700; color: var(--navy); line-height: 37px; }
  .body-text { font-size: 13.8px; line-height: 21.7px; font-weight: 300; color: var(--text); }
  .col-title { font-size: 14px; font-weight: 700; color: var(--red); }
  .small-text { font-size: 12.5px; line-height: 20px; font-weight: 300; color: var(--text); }
  .card { position: absolute; width: 292px; background: var(--card); box-shadow: 0 6px 20px rgba(0,0,0,.05); }
  .card .photo { height: 133px; }
  .card .body { padding: 25px 25px 28px; }
  .card h3 { font-size: 14.5px; font-weight: 700; color: var(--red); margin-bottom: 14px; line-height: 18px; }
  .card p { font-size: 12.5px; line-height: 20px; font-weight: 300; }
</style>
</head>
<body>
  <svg class="shape" width="1200" height="3288" aria-hidden="true">
    <path d="M41 648 L210 790 Q250 830 225 875 L41 1194 Z" fill="var(--red)"/>
    <path d="M1200 1430 L980 1615 Q940 1660 975 1705 L1200 2043 Z" fill="var(--navy)"/>
    <path d="M1200 2700 L1000 2880 Q960 2923 995 2968 L1200 3204 Z" fill="var(--red)"/>
  </svg>

  <svg class="shape" width="1200" height="470" role="img" aria-label="Foto: drei Mitarbeiter des Teams vor einem Fenster im Büro">
    <defs>
      <linearGradient id="heroPhoto" x1="0" y1="0" x2="1" y2="1">
        <stop offset="0" stop-color="#e3e6ea"/>
        <stop offset="0.55" stop-color="#c4c9cf"/>
        <stop offset="1" stop-color="#b59e6c"/>
      </linearGradient>
    </defs>
    <path d="M485 0 L1200 0 L1200 295 L935 450 Q900 470 875 445 L715 255 Z" fill="url(#heroPhoto)"/>
  </svg>

  <svg class="shape" width="340" height="3288" role="img" aria-label="Foto: Hand zeichnet ein Ablaufdiagramm auf ein Whiteboard">
    <defs>
      <linearGradient id="boardPhoto" x1="0" y1="0" x2="1" y2="1">
        <stop offset="0" stop-color="#f0f1f3"/>
        <stop offset="1" stop-color="#d6d9de"/>
      </linearGradient>
    </defs>
    <path d="M41 2975 Q200 3020 290 3150 Q330 3220 300 3288 L41 3288 Z" fill="url(#boardPhoto)"/>
  </svg>

  <div class="abs sidebar-line"></div>
  <div class="abs dots"><span class="active"></span><span></span><span></span><span></span><span></span><span></span><span></span></div>

  <div class="abs logo">ValenzWerk<i></i></div>

  <h1 class="abs hero-title">Bereit für das nächste Element<br>der Suchmaschinenoptimierung?</h1>
  <p class="abs hero-sub">ValenzWerk ist Ihre SEO-Agentur für mehr<br>Sichtbarkeit, mehr Reichweite und mehr Traffic</p>
  <div class="abs lead-form"><span class="field">Ihre Telefonnummer</span><span class="btn">Beratung vereinbaren</span></div>

  <svg class="abs" style="left:573px;top:580px" width="54" height="54" viewBox="0 0 54 54" aria-hidden="true" fill="none" stroke="var(--red)" stroke-width="2">
    <circle cx="27" cy="27" r="5"/><circle cx="8" cy="8" r="4"/><circle cx="46" cy="8" r="4"/><circle cx="8" cy="46" r="4"/><circle cx="46" cy="46" r="4"/>
    <path d="M11 11 L23 23 M43 11 L31 23 M11 43 L23 31 M43 43 L31 31 M12 8 H42 M12 46 H42"/>
  </svg>

  <h2 class="abs center section-title" style="top:680px">Abrechnung auf Erfolgsbasis –<br>garantiert!</h2>
  <p class="abs body-text" style="left:297px;top:772px;width:606px;text-align:center">Wie jetzt? Erst bezahlen, wenn die Optimierung erfolgreich war? Genauso ist es! Als erfahrene SEO Agentur bietet wir unsere Leistungen als eine der wenigen zu 100 Prozent auf Erfolgsbasis an. Das heißt, dass Sie von uns erst dann eine Rechnung erhalten, wenn Ihre Webseite auf der 1. Seite der Suchergebnisse rankt. Durch die präzise Zielvorgabe ist sichergestellt, dass Sie keinerlei Risiko eingehen und wir wie immer unser Bestes geben. Warum wir das machen? Weil wir über Jahre hinweg die perfekte Strategie für ein besseres Ranking erforscht haben und damit bisher noch jeden Kunden nach vorne gebracht haben.</p>
  <div class="abs btn" style="left:415px;top:960px;width:370px;height:43px">Jetzt unverbindliche Beratung vereinbaren</div>

  <h3 class="abs col-title" style="left:137px;top:1134px">Was ist SEO?</h3>
  <p class="abs small-text" style="left:137px;top:1176px;width:298px">SEO steht für Search Engine Optimization, zu Deutsch Suchmaschinenoptimierung, und ist eine der wichtigsten Disziplinen im Online Marketing. Wer heute Informationen benötigt oder ein Problem lösen will, der konsultiert eine Suchmaschine – allen voran Findora. Doch eins wissen Sie selbst am besten: Kaum jemand schaut sich die Suchergebnisse außerhalb von Seite eins ein. Umso wichtiger ist es, mit seiner Webseite genau hier zu ranken. Das aber wollen viele, deshalb führt für erfolgreiche Webseiten kein Weg an der Suchmaschinenoptimierung vorbei. Wir als SEO Agentur unterstützen Sie dabei, aus den zahlreichen Elementen, die für die Suchmaschinenoptimierung notwendig sind, eine funktionierende Verbindung zu schaffen.</p>

  <svg class="abs" style="left:455px;top:1103px" width="314" height="314" role="img" aria-label="Illustration: Laborgeräte, Reagenzgläser und Moleküle im Kreis angeordnet">
    <circle cx="157" cy="157" r="155" fill="#eeeff1"/>
  </svg>

  <h3 class="abs col-title" style="left:817px;top:1134px;width:246px;text-align:right">Was bringt SEO?</h3>
  <p class="abs small-text" style="left:812px;top:1176px;width:251px;text-align:right">Eine prominente Position in den Suchergebnissen führt zu einer Kettenreaktion, die sich jeder Unternehmer wünscht. Je besser Sichtbarkeit und Reichweite, desto mehr Traffic spült Findora auf Ihre Webseite. Wir als führende SEO Agentur sorgen dafür, dass es sich dabei um qualifizierten Traffic handelt, aus dem auch zahlende Kunden werden. Dadurch steigt nicht nur Ihre Konversionsrate, sondern natürlich auch der Umsatz Ihres Unternehmens. Suchmaschinenoptimierung macht sich also bezahlt!</p>

  <h2 class="abs section-title" style="left:137px;top:1596px">Warum wir?</h2>
  <p class="abs" style="left:137px;top:1638px;font-size:19px;font-weight:300;color:var(--muted)">SEO Agentur mit Herz, Verstand und ganz viel Erfahrung</p>
  <p class="abs body-text" style="left:137px;top:1688px;width:690px;font-size:14.5px">Seit über zehn Jahren forschen wir schwerpunktmäßig an der perfekten Zusammensetzung effektiver Suchmaschinenoptimierung. Als reine SEO Agentur haben wir uns ganz bewusst dafür entschieden, nicht die gesamte Palette des Online Marketings anzubieten, sondern das, wofür unser Herz schlägt und das, was den größten und vor allem nachhaltigsten Erfolg verspricht. Seitdem ist SEO mehr als unser Forschungsgebiet. SEO ist unsere Leidenschaft. Und genau die Liebe zu dem, was wir tun, macht uns so gut, dass wir ausschließlich auf Erfolgsbasis arbeiten.</p>

  <article class="card" style="left:137px;top:1911px;height:359px">
    <div class="photo" role="img" aria-label="Foto: Anwalt am Schreibtisch" style="background:linear-gradient(135deg,#8d8f93,#3b3f48)"></div>
    <div class="body"><h3>SEO für Anwälte und Steuerberater</h3><p>Große Rechtanwalts- und Steuerberaterkanzleien dominieren den Markt. Mit SEO können sich auch kleine und regionale Anwälte, Notare, Steuer- und Unternehmensberater durchsetzen. Wir helfen Ihnen, sich online als Experte zu profilieren.</p></div>
  </article>
  <article class="card" style="left:453px;top:1911px;height:359px">
    <div class="photo" role="img" aria-label="Foto: Apotheker berät eine Kundin" style="background:linear-gradient(135deg,#e4e1dc,#9b8a78)"></div>
    <div class="body"><h3>SEO für Ärzte und Apotheker</h3><p>Ärzte und Apotheker können mit einer suchmaschinen-optimierten Webseite nicht nur neue Patienten und Kunden gewinnen, sondern diesen auch langfristig binden und ihnen zeitgemäße Serviceleistungen anbieten.</p></div>
  </article>
  <article class="card" style="left:770px;top:1911px;height:359px">
    <div class="photo" role="img" aria-label="Foto: Paket wird übergeben" style="background:linear-gradient(135deg,#eceae4,#b9a878)"></div>
    <div class="body"><h3>SEO für (Online-)Händler</h3><p>Der Online-Handel boomt, entsprechend groß ist auch die Konkurrenz. Ein Online-Shop ist noch lange kein Selbstläufer und bedarf besonderen Know-hows bei der Suchmaschinen-optimierung. Wir steigern Ihre Verkaufszahlen nachhaltig!</p></div>
  </article>

  <article class="card" style="left:137px;top:2313px;height:374px">
    <div class="photo" role="img" aria-label="Foto: Handwerker in seiner Werkstatt" style="background:linear-gradient(135deg,#b59a7a,#4a3d33)"></div>
    <div class="body"><h3>SEO für Handwerker und Dienstleister</h3><p>Wer einen Handwerker oder Dienstleister sucht, der schaut nicht mehr in dicke Branchenbücher, sondern sucht online. Ohne sichtbare Webseite sind Sie für den Kunden quasi nicht existent. Mit Local SEO lässt sich das bereits mit einfachen Mitteln und für kleines Geld ändern!</p></div>
  </article>
  <article class="card" style="left:453px;top:2313px;height:374px">
    <div class="photo" role="img" aria-label="Foto: Hand arbeitet an einem Planungsboard" style="background:linear-gradient(135deg,#2d3440,#d8dbe0)"></div>
    <div class="body"><h3>SEO für Online-Portale</h3><p>Online-Portale sind von den Suchmaschinen so abhängig wie kaum ein anderes Internetangebot. Nur wer bei Findora ganz oben steht, erhält ausreichend Traffic um zu überleben. Wir sichern die Zukunft Ihres Portals und bringen Sie in die schwarzen Zahlen.</p></div>
  </article>
  <article class="card" style="left:770px;top:2313px;height:374px">
    <div class="photo" role="img" aria-label="Foto: zwei Personen arbeiten gemeinsam am Bildschirm" style="background:linear-gradient(135deg,#4d5a6c,#c8b49a)"></div>
    <div class="body"><h3>SEO für Sie</h3><p>Es gibt keine Branche, die heutzutage ohne Suchmaschinenoptimierung auskommt. Mit zielgerichteten Maßnahmen setzen wir auch Ihr Business auf ein neues Level, ganz egal wie groß Ihr Unternehmen ist. Sprechen Sie uns noch heute an!</p></div>
  </article>

  <svg class="abs" style="left:573px;top:2788px" width="54" height="54" viewBox="0 0 54 54" aria-hidden="true" fill="none" stroke="var(--red)" stroke-width="2">
    <polygon points="27,16 37,21.5 37,32.5 27,38 17,32.5 17,21.5"/>
    <path d="M27 16 V6 M37 21.5 L46 16 M37 32.5 L46 38 M27 38 V48 M17 32.5 L8 38 M17 21.5 L8 16"/>
    <circle cx="27" cy="4" r="2.5"/><circle cx="48" cy="14" r="2.5"/><circle cx="48" cy="40" r="2.5"/><circle cx="27" cy="50" r="2.5"/><circle cx="6" cy="40" r="2.5"/><circle cx="6" cy="14" r="2.5"/>
  </svg>

  <h2 class="abs center section-title" style="top:2870px">Lassen Sie sich beraten.<br>Kostenlos und unverbindlich.</h2>
  <p class="abs body-text" style="left:296px;top:2969px;width:608px;text-align:center">Seit über zehn Jahren forschen wir schwerpunktmäßig an der perfekten Zusammensetzung effektiver Suchmaschinenoptimierung. Als reine SEO Agentur haben wir uns ganz bewusst dafür entschieden, nicht die gesamte Palette des Online Marketings anzubieten, sondern das, wofür unser Herz schlägt und das, was den größten und vor allem nachhaltigsten Erfolg verspricht. Seitdem ist SEO mehr als unser Forschungsgebiet. SEO ist unsere Leidenschaft. Und genau die Liebe zu dem, was wir tun, macht uns so gut, dass wir ausschließlich auf Erfolgsbasis arbeiten.</p>
  <div class="abs btn" style="left:429px;top:3140px;width:342px;height:43px">Jetzt unverbindliche Beratung vereinbaren</div>
</body>
</html>
```